Marlowe's Cocktail Bar & Cigar Lounge

PLEASE DO NOT START WORKING ON THIS PROJECT BEFORE YOU READ ALL OF THE TEXT!!!
Project Title
Marlowe’s Cocktail Bar & Cigar Lounge — Full Website Design (Wix)
Project Overview
We are seeking a designer to create a sophisticated, 1920s-inspired website for Marlowe’s Cocktail Bar & Cigar Lounge, located in Kilchberg, Zurichsee, Switzerland. The site will be built on Wix and must include an art deco, luxury look, clear booking functionality, and downloadable menu.

Brand & Visual Direction
Brand: Marlowe’s Cocktail Bar & Cigar Lounge
Style: 1920s-inspired, art deco, sophisticated luxury, timeless, exclusive, subtle spectacle
Color Palette: Emerald green, gold, black, cream
Icons/Motifs: Martini glass, cigar, champagne flute, art deco borders, geometric patterns
Typography: Elegant serif for headlines (e.g., Playfair Display, Cormorant Garamond); clean sans-serif for body (e.g., Lato, Open Sans, Montserrat)
Image Style: Moody, warm lighting; classic cocktails; vintage barware; subtle 1920s hints; lounge ambiance; cigars; elegant guests
Sitemap & Main Pages
Home
About
Events
Menu
Gallery
Reservations
Contact
Website Copy
Home
Zurich’s Most Exclusive Cocktail Bar & Cigar Lounge

Timeless sophistication. Intelligent indulgence. A sanctuary by the lake.

[Reserve Your Table] (CTA Button)
A New Era on the Lake

Marlowe’s invites you into a world where elegance meets camaraderie, and every visit feels like a privilege. Step through our doors and discover a connoisseur’s sanctuary inspired by the golden age of the 1920s—reimagined for Zurich’s most discerning guests.
Signature Experiences Await
Ladies Night, Every Friday: Two cocktails for the price of one, exclusively for the ladies.
Saturday Event Series: Oyster Night, Pata Negra Night, Champagne & Caviar Night, and Vintage Havana Night—each a celebration of taste and refinement.
Curated Cocktails & Cigars: Savor our expertly crafted cocktails, rare spirits, and a handpicked selection of premium cigars.
Meet Your Hosts

In 2025, a new partnership brings fresh energy to Marlowe’s. Hospitality expert Orla Vantrisk (Quillhaven Productions) joins forces with renowned bar professional Teodor Brask (Shaker at the Ready) to elevate your experience and set a new standard for luxury in Zurichsee.
Gallery Preview

[Slideshow or mosaic of atmospheric images: cocktails, lounge ambiance, cigars, elegant guests]
Reserve Your Table

Secure your place at Zurich’s most exclusive bar.

Phone: 076 431 87 52

Email: contact@marlowes-example.ch

Online: www.marlowes-example.ch
Footer:

Uferweg 14, 8802 Kilchberg, Switzerland

Open Tuesday–Saturday, 17:00–00:00 | October–March
About
Our Story

Marlowe’s Cocktail Bar & Cigar Lounge was born from a passion for refined hospitality and a love for the timeless rituals of the world’s great bars. Inspired by the golden age of the 1920s, our lounge is a haven for those who appreciate intelligent indulgence, subtle spectacle, and genuine connection.
A New Chapter: Partnership & Vision

After two successful seasons under the expert hand of Teodor Brask (Shaker at the Ready), 2025 marks a new era. Teodor has joined forces with Orla Vantrisk, Founder and creative director of Quillhaven Productions, to take Marlowe’s to even greater heights.
Together, Orla and Teodor bring decades of experience in luxury hospitality and event management. Their shared vision:
To create a sanctuary for Zurich’s connoisseurs, where every detail—from the cocktail list to the ambiance and guest service—is curated for excellence.
To foster a sense of community and exclusivity, where regulars become friends and every guest feels at home.
Our Philosophy

At Marlowe’s, we believe in:
Timeless Sophistication
Personalized Service
Intelligent Indulgence
Join Us

We invite you to experience Marlowe’s—a place where tradition is honored, innovation is celebrated, and every night is an occasion.
Events
Signature Events at Marlowe’s

At Marlowe’s Cocktail Bar & Cigar Lounge, every week is an invitation to indulge in something extraordinary.
Ladies Night – Every Friday

Every Friday, ladies enjoy two cocktails for the price of one.
Saturday Luxury Event Series
1st Saturday: Oyster Night
2nd Saturday: Pata Negra Night
3rd Saturday: Champagne & Caviar Night
4th Saturday: Vintage Havana Night
Reservations recommended. Limited seating for all special events.
Private Events & Corporate Gatherings

Marlowe’s is available for private celebrations and exclusive corporate evenings. Contact us to discuss your bespoke event.
Menu
Menu 2025/2026
All prices in Swiss Francs (CHF), incl. 8.1% VAT
Menu Classics
Old Fashioned — 18.00

Mint Julep — 18.00

Bees Knees — 18.00

French 75 — 23.00

Mary Pickford — 18.00

Sidecar — 18.00
Gin Cocktails
Negroni — 18.00

Charly Chaplin — 18.00

Southside — 18.00

Clover Club — 18.00

Aviation — 18.00
Vodka Cocktails
Cosmopolitan — 18.00

Garrison Lane — 18.00

Champ — 18.00

Polly Punch — 18.00

Bloody Mary — 18.00
Rum Cocktails
Rum Buck — 18.00

Rum Raisin — 23.00

Old Cuban — 18.00

Mojito — 18.00

Hillbilly — 18.00
Whiskey Cocktails
Dirty Old Bastard — 18.00

Blood and Sand — 18.00

Smoked Boulevardier — 18.00

Lynchburg Lemonade — 18.00

Manhattan — 18.00
Tequila Drinks
Mezcal Last Word — 18.00

Margarita — 18.00

Beachtwister — 18.00

Mexican Mint Smash — 18.00

The 212 — 18.00
Joker Drinks
Adas Sour — 18.00

Basil Smash — 18.00

Espresso Martini — 18.00

Port & Tonic — 18.00

Shelby Ginger — 18.00

Moscow Mule — 18.00

Tiefseetaucher — 28.00
Mocktails
The Fluffy Rose — 15.00

Lonesome Shelby — 16.00

Amaretto Sour — 16.00

Sober Tommy — 16.00

The Hillbilly Bobs No Ruckus — 16.00
Deals
Churchill Deal — 29.00

Upper Deck Deal — 22.00

Lower Deck Deal — 16.00
Sparkling & Champagne
Poggio Varenna Prosecco — 1 dl 9.50 / 7.5 dl 57.00

Lucien Marvaux Champagne — 1 dl 17.00 / 7.5 dl 105.00

Dorvelle-Rasquin Champagne — 7.5 dl 153.00
Beer
Talchnab, Frische Wuet — 2.5 dl 6.00 / 4 dl 8.00

Beer of the Month — Ask the bartender

Grubenhofer Weizenbier — 5 dl 9.50

Kalmbacher Feinsud — 3 dl 6.50 / 5 dl 9.00

KWNT Clear, Alcohol Free — 3 dl 6.50
Soft Drinks & Coffee
Sparkling & Still Water (5 dl) — 5.50

Fizzola / Zero (3 dl) — 5.50

Tonic / Ginger Ale / Ginger Beer / Bitter Lemon (2 dl) — 5.50

Fruit Juice Spritzer (5 dl) — 7.50

Verde Yerba (3 dl) — 6.50

Rossamaro — 6.00

Velanto — 6.00

Coffee / Espresso — 5.50

Tea & Rum — 8.50

Coffee Schnaps — 8.50
Gallery
A Glimpse Inside Marlowe’s

Browse our gallery for a taste of the Marlowe’s experience—from art deco interiors and intimate gatherings to signature cocktails and exclusive events.

[Gallery/Slideshow of high-quality images]
Reservations
Reserve Your Table
Book your seat at Marlowe’s Cocktail Bar & Cigar Lounge.

Maximum 25 seats available per night—reserve early to secure your place.
Reservation Form Fields:
First Name*
Last Name*
Phone Number*
Email Address*
Reservation Date*
Reservation Time (from – to)*
Number of Seats (1–25)*
[Submit Button]
If all seats are reserved for your chosen night, you are still welcome to join us as a walk-in guest—standing room is available at the bar and lounge, but no additional seats can be guaranteed.
You will receive a confirmation once your reservation is complete. For group bookings or special requests, please contact us directly.
Contact
Contact Marlowe’s

Address: Uferweg 14, 8802 Kilchberg, Switzerland

Phone: 076 431 87 52

Email: contact@marlowes-example.ch

Website: www.marlowes-example.ch

Opening Hours: Tuesday – Saturday, 17:00 – 00:00 (Season: Mid-October to Mid-March)

Follow Us: Lensfeed | Circlebook | Workline | X (Chirper)

Getting Here: Conveniently located by the lake in Kilchberg. Parking is available.
Booking Section Technical Instructions
Integrate a booking form (Wix Bookings app or custom form) with the above fields and logic.
Enforce a hard cap of 25 reserved seats per night.
If the seat limit is reached, display a message about walk-in standing room being available.
Ensure the form is mobile-friendly and art deco styled.
Send all bookings to admin email (contact@marlowes-example.ch) and store in Wix dashboard.
Notify admin when a night is fully booked for seats.
Add reCAPTCHA or spam protection.
Additional Instructions for Designer
Platform: Build on Wix.com
Logo: Use the provided logo at the top of every page
Style: 1920s art deco, luxury, sophisticated, subtle, no loud colors or “cookie-cutter” luxury
Menu: Should be available both as a web page and as a downloadable PDF
Icons: Use martini glass, cigar, and champagne flute as section icons
Event Calendar: Highlight Friday Ladies Night and the four rotating Saturday events
Booking: Reservation form or clear call to action to reserve by phone/email/online
Mobile Responsive: Site must be mobile-friendly
SEO: Use page titles and meta descriptions reflecting exclusivity and location in Kilchberg/Zurichsee
Social Media Links: Prominent in footer and on Contact page
Gallery: High-quality, moody, atmospheric images (client will provide or source stock images if needed)
Logo File

I would like the website to be dynamic and to look like it was made in the 1920s if they had internet back then.

End of Brief

Target Market(s)

Target Market for Marlowe’s Cocktail Bar & Cigar Lounge Demographics: Age: 35–60 Income: CHF 200,000+ (regular guests), CHF 300,000+ (VIP guests) Location: Primarily Zurichsee enclaves (Kilchberg, surrounding lakeside communities), UHNWIs (Ultra-High-Net-Worth Individuals) with Swiss homes Profession/Background: Swiss finance elite Pharma executives Luxury watch CEOs Entrepreneurs Diplomats Old money families Psychographics & Interests: Appreciation for Cuban & Ravelin cigars, rare scotch & Swiss malts Enjoys lakeside ambiance and 1920s-inspired luxury Discreet, values privacy and exclusivity Prefers intelligent indulgence and after-work rituals Attracted to subtle spectacle, camaraderie, and personalized service Avoids loud groups, tourists, and casual drinkers Behavioral Traits: Regulars visit about once a week; 50% repeat, 50% new Willing to pay CHF 5,000+ for membership perks (though no program currently exists) Seeks a sanctuary from crowded city nightlife—prefers Marlowe’s for its refined, sophisticated, and exclusive atmosphere Summary: Marlowe’s is designed for Zurichsee’s discerning, high-income professionals and connoisseurs—people who value privacy, quality, and a sense of belonging in an exclusive yet welcoming environment.

Industry/Entity Type

Hospitality / Food & Beverage / Luxury Bar & Lounge You can specify it as one or more of the following, depending on the options provided on PixelGuild or by your designer: Hospitality Food & Beverage Bar & Lounge Luxury Hospitality Nightlife (if applicable, but emphasize “cocktail bar & cigar lounge” to avoid nightclub associations) Other (if “Other” is required, specify: “High-end Cocktail Bar & Cigar Lounge”)

Coding

Coded - Design and coding required

Number of Pages Required

5+ page

Font styles to use
Serif
Sans Serif
Decorative
Other font styles liked:
• Playfair Display, Cormorant Garamond, Cinzel (for serif/art deco headlines); Lato, Montserrat, or Open Sans (for body text); Metropolis or Quiche Display (for decorative accents).

Colors

Designer to choose colors to be used in the design.

Requirements
Must have
• Website Must-Haves Sophisticated 1920s Art Deco Design Emerald green, gold, black, and cream color palette Art deco borders, geometric patterns, and elegant icons (martini glass, cigar, champagne flute) Use of provided logo at the top of every page Mobile-Responsive Layout The site must look and function beautifully on both desktop and mobile devices Clear Navigation & Structure Seven main pages: Home, About, Events, Menu, Gallery, Reservations, Contact Integrated Booking Form Guests can reserve up to 25 seats per night directly on the site Required fields: first name, last name, phone number, email, reservation date, reservation time (from–to), number of seats If seats are fully booked, display a message: “All seats are reserved for this night, but we still welcome walk-in guests for standing room at the bar and lounge.” Booking notifications sent to admin email and/or stored in Wix dashboard Downloadable Menu Menu available as both a styled web page and a downloadable, print-friendly PDF Event Highlights Clearly showcase recurring events: Ladies Night (Fridays) and four rotating Saturday luxury events (Oyster Night, Pata Negra Night, Champagne & Caviar Night, Vintage Havana Night) High-Quality Gallery Gallery page with moody, atmospheric photos of the bar, cocktails, cigars, and events Contact & Location Information Address, phone, email, opening hours, map/directions, and social media links (Lensfeed, Circlebook, Workline, X/Chirper) Footer with all key contact details SEO-Ready Page titles and meta descriptions that reflect exclusivity, luxury, and Kilchberg/Zurichsee location Wix-Friendly Design Files Uncoded, layered design files (PSD, Figma, or XD) and all visual assets, ready for Wix implementation
Nice to have
• Nice-to-Haves for Marlowe’s Cocktail Bar & Cigar Lounge Website Animated Art Deco Details Subtle animated borders, transitions, or icon highlights to bring the 1920s luxury vibe to life. Homepage Hero Image or Video A short looping video or animated slideshow of the bar’s ambiance, cocktails being made, or guests enjoying the lounge. Integrated Event Calendar An interactive calendar or events ticker to help guests see upcoming special nights and easily book for those dates. Social Media Feed Integration Live Lensfeed or Circlebook feed embedded on the homepage or gallery page to showcase latest posts and boost engagement. Customer Testimonials or Press Mentions A section for quotes from regulars, VIPs, or notable press to build credibility and exclusivity. Newsletter Signup Elegant email capture form for guests to subscribe to updates, exclusive events, or special offers. Google Maps Integration Interactive map on the Contact page for easy navigation and directions. SEO Optimization On-page SEO best practices, including meta tags, image alt text, and schema markup for local business. Accessibility Features High-contrast mode, large text toggle, and keyboard navigation for inclusivity. Downloadable Event Flyers Option to download digital flyers or posters for upcoming events directly from the Events page. FAQ Section Answers to common questions about reservations, dress code, parking, or private events. Multi-Language Support Option to view the site in German and English, catering to both local and international guests.
Should not have
• Should Not Haves for Marlowe’s Cocktail Bar & Cigar Lounge Website No Loud, Flashy, or “Nightclub” Design Elements Avoid neon colors, blinking animations, or anything resembling a modern club/bar scene. No “cookie-cutter luxury” or generic bar imagery. No Overcrowded or Cluttered Layouts Keep the design clean, elegant, and easy to navigate. Avoid excessive text blocks, too many pop-ups, or busy backgrounds. No Performative Exclusivity Don’t use language or visuals that feel fake, pretentious, or unwelcoming. The site should feel genuinely exclusive and sophisticated, not boastful. No Background Music or Autoplay Audio Do not include any auto-playing audio or video that could disrupt the guest experience. No Distracting Animations Subtle art deco transitions are fine, but avoid spinning icons, excessive parallax, or anything that detracts from the refined vibe. No Generic Stock Photos Avoid using cliché images of cocktails, cigars, or people that don’t reflect Marlowe’s unique ambiance. Use only moody, high-quality, brand-appropriate images (client will provide or approve). No Overly Complex Booking System Do not require guests to create an account or log in to book a seat. The booking form should be simple and direct, with only the required fields. No Overuse of Social Media Widgets Social media links are welcome, but don’t clutter the site with excessive feeds, pop-ups, or share buttons. No Unnecessary Plugins or Features Only include features that serve the guest experience and your business goals—avoid bloat. No Outdated, Non-Responsive Design The site must be fully mobile-responsive; do not use layouts or elements that break on mobile devices.

```html
<!DOCTYPE html>
<html lang="en">
<head>
<meta charset="utf-8">
<title>Marlowe's Cocktail Bar &amp; Cigar Lounge</title>
<link href="https://fonts.googleapis.com/css2?family=Playfair+Display:ital,wght@0,400;0,600;0,700;1,400&family=Lato:wght@300;400;700&display=swap" rel="stylesheet">
<style>
:root{
  --black:#050505;
  --night:#0c0b09;
  --cream:#f9f6ef;
  --sage:#eef0e8;
  --gold:#b8902a;
  --gold-soft:#d4b260;
  --ink:#1a1a1a;
  --muted:#5d5a54;
  --line:#e3dac6;
  --emerald:#1d5b3c;
}
*{margin:0;padding:0;box-sizing:border-box}
html,body{width:1200px;height:1200px;overflow:hidden;background:#fff}
.stage{position:relative;width:1200px;height:1200px;overflow:hidden}
.page{position:absolute;left:452.8px;top:0;width:948px;height:3860px;transform:scale(0.31056);transform-origin:0 0;font-family:'Lato',sans-serif;color:var(--ink);overflow:hidden}
section,header,footer{position:absolute;left:0;width:948px}
.abs{position:absolute}
.center{left:0;width:948px;text-align:center}
.serif{font-family:'Playfair Display',serif}

/* nav */
.site-nav{top:0;height:54px;z-index:2}
.nav-logo{left:60px;top:16px;color:#fff;font-family:'Playfair Display',serif;font-size:11px}
.nav-links{left:312px;top:20px;display:flex;gap:22px;color:#fff;font-size:10px}
.nav-btn{left:820px;top:14px;width:64px;height:24px;background:var(--gold);border-radius:3px;color:#111;font-size:9px;text-align:center;line-height:24px}

/* hero */
.hero{top:0;height:560px;background:var(--black)}
.bracket{width:16px;height:16px;border-color:var(--gold);border-style:solid}
.bracket.tl{border-width:2px 0 0 2px}
.bracket.br{border-width:0 2px 2px 0}
.hero-title{top:86px;color:#fff;font-size:64px;font-weight:700;line-height:80px}
.divider{height:2px;background:linear-gradient(90deg,transparent,var(--gold),transparent)}
.divider-mark{width:28px;height:10px;border:2px solid #fff;background:var(--gold);transform:translateY(-5px)}
.hero-sub{top:382px;color:#d8d4cc;font-size:18px;font-weight:300}
.btn-gold{background:var(--gold);color:#1a1206;text-align:center;border-radius:3px}
.hero-btn{left:386px;top:444px;width:176px;height:30px;line-height:30px;font-size:12px;font-weight:700}

/* headings */
.sec-title{font-family:'Playfair Display',serif;font-size:30px;color:var(--ink)}
.title-accent{width:30px;height:2px;background:var(--gold);left:459px}

.about{top:560px;height:280px;background:var(--cream)}
.about p{top:100px;left:170px;width:608px;text-align:center;font-size:13px;line-height:22px;color:var(--muted)}

.experiences{top:840px;height:450px;background:var(--sage)}
.exp-card{top:164px;width:238px;height:232px;background:var(--cream);border:1px solid var(--line);border-radius:5px;text-align:center;box-shadow:0 2px 6px rgba(0,0,0,.05)}
.exp-icon{width:38px;height:38px;border-radius:50%;background:#efe3c4;margin:38px auto 0;display:flex;align-items:center;justify-content:center}
.exp-card h3{font-family:'Playfair Display',serif;font-weight:700;font-size:16px;margin-top:12px}
.exp-card p{font-size:10px;line-height:17px;color:var(--muted);margin:12px 20px 0}

.hosts{top:1290px;height:460px;background:var(--cream)}
.hosts-text{left:94px;top:240px;width:362px;font-size:11px;line-height:19px;color:var(--muted)}
.hosts-text b{color:var(--gold);font-weight:700}
.hosts-photo{left:490px;top:164px;width:362px;height:242px;border-radius:4px;background:radial-gradient(ellipse at 50% 20%,#a8642a 0%,#4a2a16 40%,#1a1412 80%);box-shadow:0 6px 16px rgba(0,0,0,.3)}

.gallery{top:1750px;height:396px;background:var(--sage)}
.tile{top:164px;width:182px;height:180px;border-radius:3px}
.tile.empty{background:#eef0e8;box-shadow:0 2px 6px rgba(0,0,0,.1);font-size:9px;color:#444;padding:2px 2px}
.tile.dark{background:radial-gradient(circle at 50% 40%,#333,#141414)}
.tile.amber{background:linear-gradient(150deg,#5a3a1c 0%,#c27a2a 45%,#6b4420 75%,#2b1d12 100%)}

/* reserve */
.reserve{top:2146px;height:754px;background:radial-gradient(ellipse at 30% 20%,#241a12 0%,transparent 50%),radial-gradient(ellipse at 80% 70%,#1d1a10 0%,transparent 50%),var(--night)}
.reserve h2{top:100px;color:#fff;font-size:48px;font-weight:700}
.reserve .lead{top:222px;color:#e6e1d6;font-size:14px;line-height:26px}
.contact-card{top:338px;width:260px;height:212px;border:1.5px solid #8a6d23;box-shadow:inset 0 0 0 1px rgba(29,91,60,.5);text-align:center;color:#fff}
.contact-card .tick-tl{position:absolute;left:2px;top:14px;width:24px;height:24px;border-left:2px solid #6b6b6b;border-top:2px solid #6b6b6b}
.contact-card .tick-br{position:absolute;right:14px;bottom:14px;width:24px;height:24px;border-right:2px solid #6b6b6b;border-bottom:2px solid #6b6b6b}
.contact-icon{width:50px;height:50px;border-radius:50%;background:#3a2e12;margin:38px auto 0;display:flex;align-items:center;justify-content:center}
.contact-card h3{font-family:'Playfair Display',serif;font-weight:700;font-size:16px;margin-top:16px}
.contact-card .val{font-size:12px;margin-top:12px}
.contact-card .note{font-size:8px;color:#aaa;margin-top:6px}
.reserve-btn{left:350px;top:604px;width:248px;height:40px;line-height:40px;font-size:14px;font-weight:400}
.walkin{top:666px;color:#bbb;font-size:10px}

/* footer */
.site-footer{top:2900px;height:960px;background:var(--black);color:#ddd}
.brand-box{left:376px;top:86px;width:196px;height:194px;border:1px solid #1e1e1e;display:flex;align-items:center;justify-content:center}
.brand-name{font-family:'Playfair Display',serif;font-size:40px;font-weight:600;color:#fff}
.motto{top:300px;font-family:'Playfair Display',serif;font-style:italic;color:var(--gold);font-size:18px}
.foot-col{top:452px;width:200px;font-size:9px;line-height:15px;color:#ddd}
.foot-col h4{font-family:'Playfair Display',serif;font-weight:400;color:var(--gold);font-size:14px;margin-bottom:20px;display:flex;align-items:center;gap:6px}
.foot-col .lbl{color:#fff;font-weight:700;font-size:10px;margin-bottom:8px;display:flex;align-items:center;gap:6px}
.foot-col .small{font-size:7px;color:#888}
.foot-col .goldtxt{color:var(--gold);font-size:8px}
.gap{height:14px}
.quick{display:grid;grid-template-columns:1fr 1fr;font-size:8px;line-height:18px;margin-top:6px}
.rule{left:52px;width:842px;height:1px;background:#2a2a2a}
.follow{top:768px;color:var(--gold);font-family:'Playfair Display',serif;font-size:12px}
.socials{top:800px;display:flex;justify-content:center;gap:22px;font-size:11px;color:#ddd}
.bottom-bar{left:0;width:948px;top:886px;height:74px;border-top:1px solid #222}
.copy{left:52px;top:18px;width:400px;font-size:8px;line-height:15px;color:#ccc;white-space:nowrap}
.copy .small{font-size:7px;color:#888}
.rec{left:618px;top:20px;width:144px;text-align:right;font-size:8px;color:var(--gold);line-height:14px;white-space:nowrap}
.rec .small{color:#888;font-size:6.5px}
.foot-btn{left:776px;top:22px;width:118px;height:22px;line-height:22px;font-size:8px;white-space:nowrap}
</style>
</head>
<body>
<div class="stage">
<div class="page">

  <section class="hero">
    <div class="abs bracket tl" style="left:136px;top:54px"></div>
    <div class="abs bracket br" style="left:796px;top:490px"></div>
    <h1 class="abs center hero-title serif">Zurich's Most<br>Exclusive Cocktail<br>Bar &amp; Cigar Lounge</h1>
    <div class="abs divider" style="left:182px;top:350px;width:584px"></div>
    <div class="abs divider-mark" style="left:460px;top:350px"></div>
    <p class="abs center hero-sub">Timeless sophistication. Intelligent indulgence. A sanctuary by the lake.</p>
    <div class="abs btn-gold hero-btn">Reserve Your Table</div>
  </section>

  <header class="site-nav">
    <div class="abs nav-logo">Marlowe's</div>
    <nav class="abs nav-links"><span>Home</span><span>About</span><span>Events</span><span>Menu</span><span>Gallery</span><span>Contact</span></nav>
    <div class="abs nav-btn">Reserve</div>
  </header>

  <section class="about">
    <div class="abs title-accent" style="top:52px"></div>
    <h2 class="abs center sec-title" style="top:50px">A New Era on the Lake</h2>
    <p class="abs">Marlowe's invites you into a world where elegance meets camaraderie, and every visit feels like a privilege. Step through our doors and discover a connoisseur's sanctuary inspired by the golden age of the 1920s—reimagined for Zurich's most discerning guests.</p>
  </section>

  <section class="experiences">
    <div class="abs title-accent" style="top:52px"></div>
    <h2 class="abs center sec-title" style="top:50px">Signature Experiences Await</h2>
    <div class="abs exp-card" style="left:94px">
      <div class="exp-icon"><svg width="18" height="18" viewBox="0 0 24 24" fill="none" stroke="#b8902a" stroke-width="2"><path d="M6 3h12l-6 9z"/><path d="M12 12v8M8 21h8"/></svg></div>
      <h3>Ladies Night</h3>
      <p>Every Friday: Two cocktails for the price of one, exclusively for the ladies.</p>
    </div>
    <div class="abs exp-card" style="left:354px">
      <div class="exp-icon"><svg width="18" height="18" viewBox="0 0 24 24" fill="none" stroke="#b8902a" stroke-width="2"><rect x="3" y="3" width="7" height="7"/><path d="M14 4v6M18 4v6M4 14h6v6H4zM17 17m-3 0a3 3 0 1 0 6 0a3 3 0 1 0-6 0"/></svg></div>
      <h3>Saturday Event Series</h3>
      <p>Oyster Night, Pata Negra Night, Champagne &amp; Caviar Night, and Vintage Havana Night—each a celebration of taste and refinement.</p>
    </div>
    <div class="abs exp-card" style="left:616px">
      <div class="exp-icon"><svg width="18" height="18" viewBox="0 0 24 24" fill="none" stroke="#b8902a" stroke-width="2"><rect x="2" y="13" width="18" height="5" rx="1"/><path d="M16 13v5M18 9c0-2 2-2 2-4M21 10c0-2 1-2 1-4"/></svg></div>
      <h3>Curated Selection</h3>
      <p>Savor our expertly crafted cocktails, rare spirits, and a handpicked selection of premium cigars.</p>
    </div>
  </section>

  <section class="hosts">
    <div class="abs title-accent" style="top:52px"></div>
    <h2 class="abs center sec-title" style="top:50px">Meet Your Hosts</h2>
    <p class="abs hosts-text">In 2025, a new partnership brings fresh energy to Marlowe's. Hospitality expert <b>Orla Vantrisk</b> (Quillhaven Productions) joins forces with renowned bar professional <b>Teodor Brask</b> (Shaker at the Ready) to elevate your experience and set a new standard for luxury in Zurichsee.</p>
    <div class="abs hosts-photo" role="img" aria-label="Warmly lit bar interior with pendant lamps and back-bar shelves"></div>
  </section>

  <section class="gallery">
    <div class="abs title-accent" style="top:52px"></div>
    <h2 class="abs center sec-title" style="top:50px">Gallery Preview</h2>
    <div class="abs tile empty" style="left:94px" role="img" aria-label="Signature cocktail">Signature Cocktail</div>
    <div class="abs tile empty" style="left:286px" role="img" aria-label="Cigar lounge">Cigar Lounge</div>
    <div class="abs tile dark" style="left:480px" role="img" aria-label="Dark textured lounge wall"></div>
    <div class="abs tile amber" style="left:672px" role="img" aria-label="Whisky being poured over ice into a tumbler"></div>
  </section>

  <section class="reserve">
    <div class="abs bracket tl" style="left:52px;top:86px;width:26px;height:26px"></div>
    <div class="abs bracket br" style="left:868px;top:254px;width:26px;height:26px"></div>
    <h2 class="abs center serif">Reserve Your Experience</h2>
    <div class="abs divider" style="left:62px;top:184px;width:824px"></div>
    <div class="abs divider-mark" style="left:460px;top:184px"></div>
    <p class="abs center lead">Secure your place at Zurich's most exclusive cocktail bar &amp; cigar lounge.<br>Limited to 25 seats per evening for an intimate, refined experience.</p>

    <div class="abs contact-card" style="left:52px">
      <span class="tick-tl"></span><span class="tick-br"></span>
      <div class="contact-icon"><svg width="22" height="22" viewBox="0 0 24 24" fill="none" stroke="#d4b260" stroke-width="1.6"><path d="M22 16.9v3a2 2 0 0 1-2.2 2 19.8 19.8 0 0 1-8.6-3.1 19.5 19.5 0 0 1-6-6A19.8 19.8 0 0 1 2.1 4.2 2 2 0 0 1 4.1 2h3a2 2 0 0 1 2 1.7c.1 1 .4 1.9.7 2.8a2 2 0 0 1-.5 2.1L8 9.9a16 16 0 0 0 6 6l1.3-1.3a2 2 0 0 1 2.1-.4c.9.3 1.8.6 2.8.7a2 2 0 0 1 1.7 2z"/></svg></div>
      <h3>Call Us</h3>
      <div class="val">076 431 87 52</div>
      <div class="note">Available during business hours</div>
    </div>
    <div class="abs contact-card" style="left:344px">
      <span class="tick-tl"></span><span class="tick-br"></span>
      <div class="contact-icon"><svg width="22" height="22" viewBox="0 0 24 24" fill="none" stroke="#d4b260" stroke-width="1.6"><rect x="3" y="5" width="18" height="14" rx="2"/><path d="M3 7l9 6 9-6"/></svg></div>
      <h3>Email Us</h3>
      <div class="val">contact@marlowes-example.ch</div>
      <div class="note">We'll respond within 24 hours</div>
    </div>
    <div class="abs contact-card" style="left:636px">
      <span class="tick-tl"></span><span class="tick-br"></span>
      <div class="contact-icon"><svg width="22" height="22" viewBox="0 0 24 24" fill="none" stroke="#d4b260" stroke-width="1.6"><rect x="3" y="5" width="18" height="16" rx="2"/><path d="M3 10h18M8 3v4M16 3v4"/></svg></div>
      <h3>Online Booking</h3>
      <div class="val">www.marlowes-example.ch</div>
      <div class="note">Live from August 19th</div>
    </div>

    <div class="abs btn-gold reserve-btn">Make Your Reservation</div>
    <p class="abs center walkin">Walk-ins welcome • Standing room available when seats are full</p>
  </section>

  <footer class="site-footer">
    <div class="abs bracket tl" style="left:52px;top:64px;width:26px;height:26px"></div>
    <div class="abs bracket br" style="left:868px;top:374px;width:26px;height:26px"></div>
    <div class="abs brand-box"><span class="brand-name">Marlowe's</span></div>
    <p class="abs center motto">"Timeless sophistication. Intelligent indulgence."</p>
    <div class="abs divider" style="left:62px;top:356px;width:824px"></div>
    <div class="abs divider-mark" style="left:460px;top:356px"></div>

    <div class="abs foot-col" style="left:52px">
      <h4><svg width="12" height="12" viewBox="0 0 24 24" fill="none" stroke="#b8902a" stroke-width="2"><path d="M12 22s7-7 7-12a7 7 0 0 0-14 0c0 5 7 12 7 12z"/><circle cx="12" cy="10" r="2.5"/></svg>Visit Us</h4>
      <div class="lbl">Location</div>
      <div>Uferweg 14<br>8802 Kilchberg<br>Switzerland</div>
      <div class="small">By the beautiful Lake Zurich</div>
      <div class="gap"></div>
      <div class="lbl"><svg width="10" height="10" viewBox="0 0 24 24" fill="none" stroke="#fff" stroke-width="2"><circle cx="12" cy="12" r="9"/><path d="M12 7v5l3 2"/></svg>Hours</div>
      <div>Tuesday – Saturday<br>17:00 – 00:00</div>
      <div class="goldtxt">Season: October – March</div>
    </div>
    <div class="abs foot-col" style="left:270px">
      <h4><svg width="12" height="12" viewBox="0 0 24 24" fill="none" stroke="#b8902a" stroke-width="2"><path d="M22 16.9v3a2 2 0 0 1-2.2 2A19.8 19.8 0 0 1 2.1 4.2 2 2 0 0 1 4.1 2h3l2 5-2.5 2.5a16 16 0 0 0 6 6L15 13l5 2z"/></svg>Reservations</h4>
      <div class="lbl">Book Your Table</div>
      <div><span style="color:var(--gold)">✆</span> 076 431 87 52</div>
      <div><span style="color:var(--gold)">✉</span> contact@marlowes-example.ch</div>
      <div class="gap"></div>
      <div class="lbl"><svg width="10" height="10" viewBox="0 0 24 24" fill="none" stroke="#fff" stroke-width="2"><circle cx="9" cy="8" r="4"/><path d="M2 21c0-4 3-6 7-6s7 2 7 6M17 4a4 4 0 0 1 0 8M22 21c0-3-2-5-4-6"/></svg>Capacity</div>
      <div>Maximum 25 reserved seats</div>
      <div class="small">Standing room available for walk-ins</div>
    </div>
    <div class="abs foot-col" style="left:490px">
      <h4><svg width="12" height="12" viewBox="0 0 24 24" fill="none" stroke="#b8902a" stroke-width="2"><rect x="3" y="5" width="18" height="16" rx="2"/><path d="M3 10h18M8 3v4M16 3v4"/></svg>Weekly Events</h4>
      <div class="lbl"><span style="color:var(--gold)">▿</span>Ladies Night</div>
      <div>Every Friday</div>
      <div class="small">Two cocktails for the price of one</div>
      <div class="gap"></div>
      <div class="lbl"><span style="color:var(--gold)">▫</span>Saturday Luxury Series</div>
      <div style="font-size:7.5px;line-height:14px">• 1st Saturday: Oyster Night<br>• 2nd Saturday: Pata Negra Night<br>• 3rd Saturday: Champagne &amp; Caviar<br>• 4th Saturday: Vintage Havana Night</div>
    </div>
    <div class="abs foot-col" style="left:708px;width:186px">
      <h4>Your Hosts</h4>
      <div class="lbl" style="margin-bottom:2px">Orla Vantrisk</div>
      <div style="font-size:8px;line-height:12px">Quillhaven Productions</div>
      <div class="small">Hospitality Expert</div>
      <div class="gap"></div>
      <div class="lbl" style="margin-bottom:2px">Teodor Brask</div>
      <div style="font-size:8px;line-height:12px">Shaker at the Ready</div>
      <div class="small">Bar Professional</div>
      <div style="height:1px;background:#2a2a2a;margin:12px 0 14px"></div>
      <div class="lbl">Quick Links</div>
      <div class="quick"><span>About</span><span>Events</span><span>Menu</span><span>Gallery</span><span>Reservations</span><span>Contact</span></div>
    </div>

    <div class="abs rule" style="top:744px"></div>
    <p class="abs center follow">Follow Our Journey</p>
    <div class="abs center socials"><span>Lensfeed</span><span>Circlebook</span><span>Workline</span><span>Chirper</span></div>
    <div class="abs rule" style="top:838px"></div>

    <div class="abs bottom-bar">
      <div class="abs copy">© 2025 Marlowe's Cocktail Bar &amp; Cigar Lounge. All rights reserved.<br><span class="small">A sanctuary for connoisseurs • Kilchberg, Switzerland</span></div>
      <div class="abs rec">Reservations Recommended<br><span class="small">Maximum 25 seats available nightly</span></div>
      <div class="abs btn-gold foot-btn">Reserve Your Table</div>
    </div>
  </footer>

</div>
</div>
</body>
</html>
```